GLINT GIN BY TIDE LURE CO

We plan to use a rum product from the caribbean country of Belize CA. That will need to be mentioned somewhere on the label. We want to do a more high-line product, an aged dark rum that plays on the shark theme. We want to use a sleek bottle design with a clever label. Or unique label placement. We need something that will pop off the shelf. We want you to have fun with it and see where it goes. We like the idea of sharks circling around the bottle, possibly like an etching on the glass or back printed on the label or a clear label that can feature the sharks in some capacity. (Not a must) "Chum" because it attracts sharks.

The "Glint Gin" needs a FONT that can become synonymous with the word and then the product. Glint Gin is to be the focus and Tide Lure Co is merely the parent company and requires mention.
Ex:
Tide Lure co.'s Glint Gin
produced in Belize, CA
or Glint Gin produced in Belize for
Tide Lure co.

We have a Glint Gin "mascot" or stamp that is a tribal shark drawing that we want used in the designs where ever you feel fit. We like the stamp as it is, but if you have some tweaks we may consider them.
Updates

I have increased first place to $450.00  and 2nd place to$150.00 !!!

 Everything we have gotten has been great just looking for more ideas. Looking for something sharp and sleek for our bottle we are trying to sell a  upscale rum !! We need it for a aged rum & a white rum .. 

  Thank you !! 
  Torvin

Target Market(s)

MALE 25 TO 45

Industry/Entity Type

It Company

Requirements
Must have
• SHARK THEME ...
Should not have
• OLD WORLD LOOK / MAP LOOKING / TRADITIONAL/ CHEAP.
We don't want everything that has already been done, like all the pirate themes. You can hint at any of these elements in a clever understated way. It is rum after all!

```html
<!DOCTYPE html>
<html lang="en">
<head>
<meta charset="utf-8">
<title>Glint Gin – Bottle Label</title>
<link rel="stylesheet" href="https://fonts.googleapis.com/css2?family=Open+Sans:wght@400;600&display=swap">
<style>
  :root {
    --backdrop: #f1f1f1;
    --amber-light: #df8442;
    --amber-deep: #a8240f;
    --amber-mid: #c24a1c;
    --amber-edge: #e07d12;
    --shoulder-dark: #1f1f1f;
    --shoulder-soft: #3a3a3a;
    --cap-black: #17232a;
    --neck-red: #d7141a;
    --glass-clear: #e6ecef;
    --ink-white: #ffffff;
    --bar-black: #000000;
    --silhouette-red: rgba(110, 18, 10, 0.45);
  }
  html, body {
    margin: 0;
    padding: 0;
    width: 1200px;
    height: 1000px;
    overflow: hidden;
    background: var(--backdrop);
  }
  .bottle-canvas {
    display: block;
    width: 1200px;
    height: 1000px;
  }
  .label-text {
    font-family: "Open Sans", sans-serif;
    fill: var(--ink-white);
  }
  .brand-name { font-size: 28px; font-weight: 600; letter-spacing: 1.5px; }
  .neck-brand { font-size: 12px; font-weight: 600; letter-spacing: 1px; }
  .tagline { font-size: 17px; font-weight: 400; }
  .producer-line { font-size: 10px; opacity: 0.85; }
  .volume-text { font-size: 8.5px; font-weight: 600; }
</style>
</head>
<body>
<svg class="bottle-canvas" viewBox="0 0 1200 1000" xmlns="http://www.w3.org/2000/svg">
  <defs>
    <linearGradient id="amber-body" x1="0" y1="0" x2="1" y2="0">
      <stop offset="0" stop-color="var(--amber-light)"/>
      <stop offset="0.35" stop-color="var(--amber-mid)"/>
      <stop offset="0.55" stop-color="var(--amber-deep)"/>
      <stop offset="0.8" stop-color="var(--amber-mid)"/>
      <stop offset="1" stop-color="var(--amber-edge)"/>
    </linearGradient>
    <linearGradient id="shoulder-fill" x1="0" y1="0" x2="1" y2="0">
      <stop offset="0" stop-color="var(--shoulder-dark)"/>
      <stop offset="0.6" stop-color="var(--shoulder-soft)"/>
      <stop offset="1" stop-color="var(--shoulder-dark)"/>
    </linearGradient>
  </defs>

  <!-- clear glass base -->
  <path class="glass-base" d="M478 860 L722 860 L722 898 Q722 925 696 925 L504 925 Q478 925 478 898 Z" fill="var(--glass-clear)"/>

  <!-- amber liquid body -->
  <path class="bottle-body" d="M478 330 L722 330 L722 872 Q722 880 712 880 L488 880 Q478 880 478 872 Z" fill="url(#amber-body)"/>

  <!-- dark neck and shoulder area -->
  <path class="bottle-shoulder" role="img" aria-label="Shark jaw illustration wrapping the bottle shoulder"
        fill="url(#shoulder-fill)"
        d="M567 72 L633 72 L633 240 Q640 268 690 282 Q722 296 722 330 L722 420
           L478 420 L478 330 Q478 296 510 282 Q560 268 567 240 Z"/>

  <!-- cap -->
  <rect class="bottle-cap" x="567" y="72" width="66" height="118" rx="4" fill="var(--cap-black)"/>

  <!-- neck label -->
  <rect class="neck-label" x="578" y="72" width="44" height="136" fill="var(--neck-red)"/>
  <text class="label-text neck-brand" transform="translate(605 84) rotate(90)">GLINT GIN</text>

  <!-- brand name -->
  <text class="label-text brand-name" x="600" y="626" text-anchor="middle">GLINT GIN</text>

  <!-- shark mascot illustration area -->
  <g role="img" aria-label="Faint tribal shark mascot illustration">
    <ellipse cx="600" cy="690" rx="64" ry="52" fill="var(--silhouette-red)"/>
  </g>

  <!-- taglines -->
  <text class="label-text tagline" x="610" y="766" text-anchor="middle" letter-spacing="8">Premium</text>
  <text class="label-text tagline" x="603" y="784" text-anchor="middle" letter-spacing="0">Crafted Aged Rum</text>
  <text class="label-text tagline" x="610" y="802" text-anchor="middle" letter-spacing="3.8">from Belize</text>
  <text class="label-text producer-line" x="601" y="818" text-anchor="middle" letter-spacing="1.6">Tide Lure co.'s Glint Gin</text>
  <text class="label-text producer-line" x="601" y="830" text-anchor="middle" letter-spacing="1.6">produced in Belize, CA</text>

  <!-- volume bar -->
  <rect class="volume-bar" x="531" y="836" width="144" height="14" fill="var(--bar-black)"/>
  <text class="label-text volume-text" x="535" y="846">40% Alcohol.</text>
  <text class="label-text volume-text" x="671" y="846" text-anchor="end">750 ml.</text>
</svg>
</body>
</html>
```